QLV Fashion Design Company Needs a New Web Design, Please Click Me

Designers:

PLEASE NOTE: we only need the web page design, not a fully coded website.

Our brand's name is The Bright Quarry, our signature is print. our style is edgy and chic.

The old website is too messy. here's the address:
www.qlvstudio.com.cn

The new website's purpose is to show our brand/design and most importantly, sell products, So it should be a combination of a designer official website and online shopping. I want the whole style to be clean, edgy and pioneer, easy to understand. we need a sophisticated online shopping website.

The reference websites are:
merolatest.co.uk
www.pd-kor.com
lucasvemm.com
orbaduvi.com
talumerosapkin.com

Please beat their designs :)

Check out our lasted fashion show to get to know us more.

https://www.vidplexa.com/watch?v=ZkamWtrBnoLe&spfreload=10

The attachments are our Logo and some 2015 Look Book.
(Please let us know if you want to play with our print in this particular web design, we can send the source file.)
Updates

Designers, we really like the design of ameliadrovenko.com(we have attached a picture of the website) , Can we get a homepage like that? so the designs you submit will be 3 pages. The first one should be a page that only has Shop/Look. then the shop page, it should be nothing but our product which we will list the categories ourself. And the look page should contain all the info. such as news, about us and designers etc. Thank you all for your hard work, we really enjoyed the designs. Added Monday, November 03, 2014

Target Market(s)

Our target audiences are woman aged from 16-40 who like online shopping

Industry/Entity Type

Online Shopping

Number of Pages Required

3 page

Font styles to use
Serif
Sans Serif
Script

Requirements
Must have
• Designers,
• we really like the design of ameliadrovenko.com(we have attached a picture of the website) , Can we get a homepage like that? so the designs you submit will be 3 pages. The first one should be a page that only has Shop/Look. then the shop page, it should be nothing but our product which we will list the categories ourself. And the look page should contain all the info. such as news, about us and designers etc. Thank you all for your hard work, we really enjoyed the designs.

```html
<!DOCTYPE html>
<html lang="en">
<head>
<meta charset="utf-8">
<title>QLV Group — The Bright Quarry</title>
<link rel="stylesheet" href="https://fonts.googleapis.com/css2?family=EB+Garamond:wght@400&family=Lato:wght@300;400&display=swap">
<style>
  :root {
    --ink: #1b1b1b;
    --accent: #e0313a;
    --panel: rgba(255, 255, 255, 0.96);
    --button-border: #dcdcdc;
    --footer-text: #ededed;
    --icon: #f4f4f4;
    --photo-light: #b9b9b9;
    --photo-mid: #7d7d7d;
    --photo-dark: #3e3e3e;
  }
  * { box-sizing: border-box; margin: 0; padding: 0; }
  html, body { width: 1200px; height: 938px; overflow: hidden; }
  body { position: relative; font-family: "Lato", sans-serif; background: var(--photo-mid); }

  .hero-photo {
    position: absolute; inset: 0;
    background:
      radial-gradient(ellipse 180px 420px at 560px 560px, rgba(20,20,20,0.55), transparent 70%),
      radial-gradient(ellipse 200px 240px at 560px 200px, rgba(235,235,235,0.35), transparent 70%),
      linear-gradient(90deg, var(--photo-light) 0%, #cfcfcf 18%, var(--photo-dark) 26%, #555 45%, var(--photo-mid) 62%, #6a6a6a 80%, #4a4a4a 100%);
  }

  .entry-panel {
    position: absolute; left: 458px; top: 253px; width: 283px; height: 375px;
    background: var(--panel);
    text-align: center;
  }
  .brand-mark {
    position: absolute; left: 50%; top: 40px; transform: translateX(-50%);
    width: 94px; height: 94px; border-radius: 50%; background: var(--accent);
  }
  .brand-name {
    position: absolute; left: 0; right: 0; top: 141px;
    font-family: "EB Garamond", serif; font-weight: 400; color: var(--ink);
    font-size: 22px; line-height: 21px; letter-spacing: 1.2px; text-transform: uppercase;
  }
  .brand-name span { display: block; }
  .brand-name .tagline { font-size: 20px; letter-spacing: 0.9px; }

  .entry-actions {
    position: absolute; left: 25px; top: 283px; display: flex; gap: 17px;
  }
  .entry-button {
    display: block; width: 108px; height: 42px; line-height: 40px;
    border: 1px solid var(--button-border); background: #fff;
    color: var(--accent); font-weight: 300; font-size: 19px;
    text-decoration: none; text-transform: uppercase; letter-spacing: 0.3px;
  }

  .social-links {
    position: absolute; top: 871px; left: 0; right: 0;
    display: flex; justify-content: center; gap: 13px;
  }
  .social-links a { display: block; width: 14px; height: 14px; background: var(--icon); border-radius: 2px; }

  .site-footer {
    position: absolute; top: 908px; left: 0; right: 0; text-align: center;
    color: var(--footer-text); font-size: 13px; font-weight: 300;
  }
</style>
</head>
<body>
  <div class="hero-photo" role="img" aria-label="Black and white photograph of a model in a white top and black skirt leaning against a weathered stone wall"></div>

  <main class="entry-panel">
    <div class="brand-mark" aria-hidden="true"></div>
    <h1 class="brand-name">
      <span>QLV Group</span>
      <span class="tagline">The Bright Quarry</span>
    </h1>
    <nav class="entry-actions">
      <a class="entry-button" href="#shop">Shop</a>
      <a class="entry-button" href="#look">Look</a>
    </nav>
  </main>

  <nav class="social-links" aria-label="Social media">
    <a href="#" aria-label="Social profile one"></a>
    <a href="#" aria-label="Social profile two"></a>
    <a href="#" aria-label="Social profile three"></a>
  </nav>

  <footer class="site-footer">Copyright © 2014 QLV Group.</footer>
</body>
</html>
```